Business Card design for shipping company 'FERNHOLT INTERNATIONAL LTD'

Classic / traditional business card in black Garamond / Times New Roman or similar text for a shipping / marine transport company, containing the following information:

QUOTE

FERNHOLT INTERNATIONAL LTD

MARTIN QUESTEDGE FICS

T: +44 7902 615370
E: cargo@fernholt-example.com

UNQUOTE

Target Market(s)

Marine / Shipping industry

Contact Information for Business Card

FERNHOLT INTERNATIONAL LTD MARTIN QUESTEDGE FICS T: +44 7902 615370 E: cargo@fernholt-example.com

Font styles to use
Serif

Colors

Designer to choose colors to be used in the design.

Requirements
Must have
• Garamond / Times New Roman or similar text in black colour

```html
<!DOCTYPE html>
<html lang="en">
<head>
<meta charset="utf-8">
<title>Fernholt International Ltd — Business Card</title>
<link rel="stylesheet" href="https://fonts.googleapis.com/css2?family=Tinos:wght@400;700&family=Poppins:wght@400;500&display=swap">
<style>
  :root {
    --backdrop: #b4b4b4;
    --navy: #0e1842;
    --navy-deep: #0a1235;
    --periwinkle: #8a9ef4;
    --white: #ffffff;
    --sea-sky: #c9cbd6;
    --sea-teal: #2f8f8a;
    --sea-deep: #1f5f66;
    --harbour-sky: #b9d3e6;
    --harbour-water: #5f7f96;
  }
  html, body {
    margin: 0;
    padding: 0;
    width: 1200px;
    height: 868px;
    overflow: hidden;
    background: var(--backdrop);
  }
  .canvas {
    position: relative;
    width: 1200px;
    height: 868px;
  }
  .card {
    position: absolute;
    left: 312px;
    width: 575px;
    height: 327px;
    background: var(--navy);
    overflow: hidden;
    box-shadow: 6px 8px 12px rgba(0, 0, 0, 0.3);
  }
  .card--front { top: 83px; }
  .card--back { top: 456px; }
  .card-shapes {
    position: absolute;
    inset: 0;
    width: 575px;
    height: 327px;
  }
  .brand-name {
    font-family: "Tinos", "Times New Roman", serif;
    color: var(--white);
    letter-spacing: 0.08em;
    margin: 0;
    line-height: 1;
  }
  .brand-tagline {
    font-family: "Poppins", sans-serif;
    color: var(--periwinkle);
    letter-spacing: 0.2em;
    margin: 0;
    line-height: 1;
  }
  .front-brand {
    position: absolute;
    left: 52px;
    top: 37px;
    text-align: center;
  }
  .front-brand .brand-name { font-size: 17px; }
  .front-brand .brand-tagline { font-size: 7px; margin-top: 4px; }
  .person {
    position: absolute;
    left: 52px;
    top: 88px;
  }
  .person-name {
    font-family: "Tinos", "Times New Roman", serif;
    font-weight: 700;
    font-size: 27px;
    line-height: 27px;
    letter-spacing: 0.04em;
    margin: 0;
    color: var(--white);
  }
  .person-name .first { color: var(--periwinkle); display: block; }
  .person-name .line { display: block; }
  .person-role {
    font-family: "Poppins", sans-serif;
    font-size: 12px;
    letter-spacing: 0.14em;
    color: var(--periwinkle);
    margin: 4px 0 0;
  }
  .contact-icons {
    position: absolute;
    left: 54px;
    top: 229px;
    width: 24px;
    height: 56px;
    border-radius: 12px;
    background: var(--periwinkle);
  }
  .contact-list {
    position: absolute;
    left: 92px;
    top: 232px;
    margin: 0;
    padding: 0;
    list-style: none;
    font-family: "Poppins", sans-serif;
    font-size: 15px;
    line-height: 24px;
    color: var(--white);
  }
  .back-brand {
    position: absolute;
    left: 0;
    width: 320px;
    top: 140px;
    text-align: center;
  }
  .back-brand .brand-name { font-size: 27px; }
  .back-brand .brand-tagline { font-size: 11px; margin-top: 6px; letter-spacing: 0.22em; }
</style>
</head>
<body>
<main class="canvas">

  <section class="card card--front">
    <svg class="card-shapes" viewBox="0 0 575 327" aria-hidden="false">
      <defs>
        <linearGradient id="port-photo-tone" x1="0" y1="0" x2="0.3" y2="1">
          <stop offset="0" stop-color="var(--sea-sky)"/>
          <stop offset="0.25" stop-color="#6aa9a6"/>
          <stop offset="0.7" stop-color="var(--sea-teal)"/>
          <stop offset="1" stop-color="var(--sea-deep)"/>
        </linearGradient>
      </defs>
      <rect class="wave-field" width="575" height="327" fill="var(--navy)" role="img" aria-label="Subtle navy wave line pattern"/>
      <path class="divider-curve" d="M318 0 C283 90 360 200 330 327 L575 327 L575 0 Z" fill="var(--white)"/>
      <path class="photo-area" d="M340 0 C305 90 382 200 350 327 L575 327 L575 0 Z" fill="url(#port-photo-tone)" role="img" aria-label="Aerial photo of a container ship alongside port cranes"/>
      <g class="contact-icon-marks" fill="none" stroke="var(--navy)" stroke-width="1.4" stroke-linecap="round" stroke-linejoin="round">
        <path d="M61.5 238 c0 5 3 9 8 10 l1.5-2 -2.5-2 -1.5 1 c-1.5-1-2.5-2-3-3.5 l1-1.5 -2-2.5 z"/>
        <rect x="60" y="264" width="12" height="9" rx="1"/>
        <path d="M60 265 l6 4.5 6-4.5"/>
      </g>
    </svg>

    <div class="front-brand">
      <p class="brand-name">FERNHOLT</p>
      <p class="brand-tagline">INTERNATIONAL LTD</p>
    </div>

    <div class="person">
      <h1 class="person-name">
        <span class="first">MARTIN</span>
        <span class="line">QUESTEDGE</span>
        <span class="line">FICS</span>
      </h1>
      <p class="person-role">OWNER</p>
    </div>

    <div class="contact-icons" style="background: transparent;"></div>
    <ul class="contact-list">
      <li class="contact-phone">+44 7902 615370</li>
      <li class="contact-email">cargo@fernholt-example.com</li>
    </ul>
  </section>

  <section class="card card--back">
    <svg class="card-shapes" viewBox="0 0 575 327">
      <defs>
        <linearGradient id="harbour-photo-tone" x1="0" y1="0" x2="0" y2="1">
          <stop offset="0" stop-color="var(--harbour-sky)"/>
          <stop offset="0.45" stop-color="#d9d3c4"/>
          <stop offset="0.62" stop-color="#9fa9b3"/>
          <stop offset="1" stop-color="var(--harbour-water)"/>
        </linearGradient>
      </defs>
      <rect class="wave-field" width="575" height="327" fill="var(--navy)" role="img" aria-label="Subtle navy wave line pattern"/>
      <path class="divider-curve" d="M310 0 C270 110 275 240 325 327 L575 327 L575 0 Z" fill="var(--white)"/>
      <path class="photo-area" d="M332 0 C292 110 297 240 347 327 L575 327 L575 0 Z" fill="url(#harbour-photo-tone)" role="img" aria-label="Photo of a harbour with cranes, passenger boats and a cargo barge"/>
    </svg>

    <div class="back-brand">
      <p class="brand-name">FERNHOLT</p>
      <p class="brand-tagline">INTERNATIONAL LTD</p>
    </div>
  </section>

</main>
</body>
</html>
```